Brightmend Outdoor Signage

We need an outdoor signage design for my company with new logo designed from artflockhub. We do electrical, Air conditioning & Plumbing, installation, service, repairs and maintenance. The design shall be an eye catching that cannot miss ready it.

Industry/Entity Type

Electrical, Air conditioning, Plumbing

```html
<!DOCTYPE html>
<html lang="en">
<head>
<meta charset="utf-8">
<title>Brightmend Outdoor Signage</title>
<link href="https://fonts.googleapis.com/css2?family=Bebas+Neue&family=Poppins:wght@600;700;800&display=swap" rel="stylesheet">
<style>
  :root {
    --brand-blue: #1d5bb0;
    --brand-red: #e3101b;
    --brand-orange: #ec8a30;
    --ink: #14161c;
    --paper: #ffffff;
    --page: #f2f2f2;
  }
  * { margin: 0; padding: 0; box-sizing: border-box; }
  html, body { width: 812px; height: 1200px; overflow: hidden; background: var(--page); }
  .canvas { position: relative; width: 812px; height: 1200px; }
  .sign {
    position: absolute; left: 26px; top: 410px; width: 760px; height: 380px;
    background: var(--paper); overflow: hidden;
    box-shadow: 0 8px 24px rgba(0,0,0,.18);
    font-family: "Poppins", sans-serif;
  }
  .sign-art { position: absolute; inset: 0; }
  .headline-top {
    position: absolute; left: 24px; top: 24px;
    font-family: "Bebas Neue", sans-serif; font-size: 37px; font-weight: 400; line-height: 1;
    color: var(--brand-blue); letter-spacing: .2px; white-space: nowrap;
  }
  .headline-main {
    position: absolute; left: 24px; top: 62px;
    font-weight: 800; font-size: 54px; line-height: 1;
    color: var(--brand-red); letter-spacing: -.5px; white-space: nowrap;
  }
  .service-label {
    position: absolute; top: 200px; width: 100px; margin-left: -50px;
    text-align: center; color: var(--paper); font-weight: 700; font-size: 11.5px;
    white-space: nowrap;
  }
  .brand-name {
    position: absolute; left: 22px; top: 302px;
    font-weight: 700; font-size: 17px; color: var(--brand-orange); line-height: 1; white-space: nowrap;
  }
  .phone {
    position: absolute; left: 188px; top: 264px;
    font-weight: 800; font-size: 32px; color: var(--brand-red); line-height: 1; white-space: nowrap;
  }
  .contact-line {
    position: absolute; left: 156px; font-weight: 700; font-size: 13px; line-height: 1.2;
    color: var(--ink); white-space: nowrap;
  }
  .contact-email { top: 303px; }
  .contact-web { top: 326px; }
</style>
</head>
<body>
<div class="canvas">
  <section class="sign">
    <svg class="sign-art" width="760" height="380" viewBox="0 0 760 380">
      <defs>
        <linearGradient id="photoTone" x1="0" y1="0" x2="1" y2="1">
          <stop offset="0" stop-color="#8f8c87"/>
          <stop offset=".45" stop-color="#c9c6c0"/>
          <stop offset="1" stop-color="#e6e2dc"/>
        </linearGradient>
      </defs>
      <rect class="service-band" x="0" y="158" width="470" height="78" fill="var(--brand-orange)"/>
      <rect class="band-rule" x="0" y="236" width="470" height="6" fill="var(--brand-red)"/>
      <rect class="footer-rule" x="0" y="368" width="480" height="12" fill="var(--brand-red)"/>
      <g class="band-dividers" stroke="#f6b27a" stroke-width="1">
        <line x1="121" y1="175" x2="121" y2="236"/>
        <line x1="210" y1="175" x2="210" y2="236"/>
        <line x1="306" y1="175" x2="306" y2="236"/>
      </g>
      <path d="M436 0 C400 80 392 200 450 270 L470 380 L480 380 L460 270 C402 200 412 80 452 0 Z" fill="var(--brand-red)"/>
      <path d="M448 0 C412 80 404 200 460 270 L480 380 L490 380 L470 270 C414 200 424 80 464 0 Z" fill="var(--brand-blue)"/>
      <path d="M460 0 C424 80 416 200 470 270 L490 380 L500 380 L480 270 C426 200 436 80 476 0 Z" fill="var(--brand-orange)"/>
      <path role="img" aria-label="Photo of a smiling tradesman in hard hat and overalls holding a wrench, with a gloved hand tightening a sink drain pipe behind him" d="M472 0 L760 0 L760 380 L500 380 L480 270 C428 200 438 80 472 0 Z" fill="url(#photoTone)"/>
      <g class="service-icons" fill="var(--brand-blue)" stroke="var(--paper)" stroke-width="3">
        <circle cx="66" cy="158" r="29"/>
        <circle cx="166" cy="158" r="29"/>
        <circle cx="261" cy="158" r="29"/>
        <circle cx="361" cy="158" r="29"/>
      </g>
      <g class="icon-glyphs" stroke="var(--paper)" stroke-width="4" stroke-linecap="round" fill="none">
        <line x1="55" y1="147" x2="77" y2="169"/>
        <line x1="77" y1="147" x2="55" y2="169"/>
        <circle cx="166" cy="158" r="10"/>
        <circle cx="166" cy="158" r="3" fill="var(--paper)"/>
        <rect x="249" y="152" width="24" height="16" rx="2" stroke-width="3"/>
        <path d="M256 152 v-4 h10 v4" stroke-width="3"/>
        <line x1="350" y1="151" x2="372" y2="151"/>
        <line x1="361" y1="151" x2="361" y2="170"/>
        <path d="M355 164 l6 6 l6 -6" stroke-width="3"/>
      </g>
      <circle cx="170" cy="281" r="10" fill="var(--brand-blue)"/>
      <path d="M166 275 l3 3 l-2 2 a8 8 0 0 0 4 4 l2 -2 l3 3 l-2 2 a10 10 0 0 1 -10 -10 z" fill="var(--paper)"/>
    </svg>

    <h1 class="headline-top">ELECTRICAL, AIR CONDITIONING</h1>
    <h2 class="headline-main">&amp; PLUMBING</h2>

    <span class="service-label" style="left:67px">INSTALLATION</span>
    <span class="service-label" style="left:166px">SERVICE</span>
    <span class="service-label" style="left:262px">REPAIRS</span>
    <span class="service-label" style="left:361px">MAINTENANCE</span>

    <div class="brand-name">Brightmend</div>

    <div class="phone">0400 555 019</div>
    <div class="contact-line contact-email">info@brightmendelectrical.com.au</div>
    <div class="contact-line contact-web">www.brightmendelectrical.com.au</div>
  </section>
</div>
</body>
</html>
```